Folder, biz cards, stationary, mailing labels, and labels containing my logo
Initiative KORVATH an engineering educational non-profit organization
Cutting-Edge
Marcus Tellfair
Executive Director
mtellfair@initiativekorvath-demo.org
www.initiativekorvath-demo.org
I will need a total of 6 business cards made.
we have a secondary logo that could be placed nicely on the back.
IK Main Logo
secondary logo that can be used on some documents

```html
<!DOCTYPE html>
<html lang="en">
<head>
<meta charset="utf-8">
<title>Initiative KORVATH – Business Card</title>
<link href="https://fonts.googleapis.com/css2?family=Roboto:wght@400;700&display=swap" rel="stylesheet">
<style>
  :root {
    --page: #e6e6e6;
    --card: #ffffff;
    --navy: #0f2c66;
    --ink: #1d2230;
    --blue: #1877e0;
    --bright: #2a8cff;
    --deep: #050a16;
    --grey: #3a3f4a;
    --rule: #d3d6dc;
  }
  * { margin: 0; padding: 0; box-sizing: border-box; }
  html, body {
    width: 1200px; height: 778px; overflow: hidden;
    background: var(--page);
    font-family: "Roboto", Arial, sans-serif;
  }
  .card {
    position: relative;
    width: 1200px; height: 778px;
    background: var(--card);
    border-radius: 40px;
    overflow: hidden;
  }
  .swoosh { position: absolute; inset: 0; width: 1200px; height: 778px; }
  .brand {
    position: absolute; left: 283px; top: 110px;
    display: flex; align-items: center; gap: 30px;
  }
  .brand-dot {
    width: 150px; height: 150px; border-radius: 50%;
    background: var(--blue);
  }
  .brand-name {
    color: var(--navy);
    font-weight: 700; font-size: 86px; line-height: 0.98;
    letter-spacing: 1px;
  }
  .person {
    position: absolute; right: 640px; top: 505px;
    text-align: right;
  }
  .person-name {
    color: var(--ink); font-weight: 700; font-size: 40px;
  }
  .person-title {
    color: var(--blue); font-weight: 700; font-size: 29px; margin-top: 6px;
  }
  .divider {
    position: absolute; left: 598px; top: 455px;
    width: 2px; height: 235px; background: var(--rule);
  }
  .contacts {
    position: absolute; left: 632px; top: 474px;
    list-style: none;
  }
  .contacts li {
    display: flex; align-items: center; gap: 12px;
    height: 48px;
    color: var(--grey); font-size: 25px;
  }
  .contacts svg { width: 24px; height: 24px; flex: none; fill: var(--blue); }
</style>
</head>
<body>
  <div class="card">
    <svg class="swoosh" viewBox="0 0 1200 778" aria-hidden="true">
      <defs>
        <linearGradient id="darkRight" x1="0" y1="0" x2="1" y2="0">
          <stop offset="0" stop-color="#0d2c6a"/>
          <stop offset="0.5" stop-color="var(--deep)"/>
          <stop offset="1" stop-color="#0b1a3a"/>
        </linearGradient>
        <linearGradient id="darkLeft" x1="0" y1="0" x2="1" y2="1">
          <stop offset="0" stop-color="var(--deep)"/>
          <stop offset="0.6" stop-color="#0e2a5e"/>
          <stop offset="1" stop-color="var(--deep)"/>
        </linearGradient>
      </defs>
      <path d="M985,0 Q1165,330 1200,760 L1200,0 Z" fill="var(--bright)"/>
      <path d="M1015,0 Q1180,320 1200,640 L1200,0 Z" fill="url(#darkRight)"/>
      <path d="M0,430 Q140,660 400,778 L0,778 Z" fill="var(--bright)"/>
      <path d="M0,470 Q120,680 320,778 L0,778 Z" fill="url(#darkLeft)"/>
    </svg>

    <div class="brand">
      <div class="brand-dot"></div>
      <div class="brand-name">Initiative<br>KORVATH</div>
    </div>

    <div class="person">
      <div class="person-name">Marcus Tellfair</div>
      <div class="person-title">Executive Director</div>
    </div>

    <div class="divider"></div>

    <ul class="contacts">
      <li>
        <svg viewBox="0 0 24 24"><path d="M6.6 10.8a15.1 15.1 0 0 0 6.6 6.6l2.2-2.2a1 1 0 0 1 1-.25 11.4 11.4 0 0 0 3.6.57 1 1 0 0 1 1 1V20a1 1 0 0 1-1 1A17 17 0 0 1 3 4a1 1 0 0 1 1-1h3.5a1 1 0 0 1 1 1c0 1.25.2 2.45.57 3.57a1 1 0 0 1-.25 1z"/></svg>
        555-014-2738
      </li>
      <li>
        <svg viewBox="0 0 24 24"><path d="M6 2h9l3 3v5H6z M3 11h18a1 1 0 0 1 1 1v6h-4v4H6v-4H2v-6a1 1 0 0 1 1-1zm5 7v2h8v-4H8z"/></svg>
        555-019-6405
      </li>
      <li>
        <svg viewBox="0 0 24 24"><path d="M3 5h18a1 1 0 0 1 1 1v12a1 1 0 0 1-1 1H3a1 1 0 0 1-1-1V6a1 1 0 0 1 1-1zm1 2.2V17h16V7.2l-8 5.3z M5 7l7 4.6L19 7z"/></svg>
        mtellfair@initiativekorvath-demo.org
      </li>
      <li>
        <svg viewBox="0 0 24 24"><path d="M12 2a10 10 0 1 0 0 20 10 10 0 0 0 0-20zm6.9 9h-3a15 15 0 0 0-1.3-5.6A8 8 0 0 1 18.9 11zM12 4.1c.9 1.2 1.8 3.6 2 6.9h-4c.2-3.3 1.1-5.7 2-6.9zM9.4 5.4A15 15 0 0 0 8.1 11h-3a8 8 0 0 1 4.3-5.6zM5.1 13h3a15 15 0 0 0 1.3 5.6A8 8 0 0 1 5.1 13zm6.9 6.9c-.9-1.2-1.8-3.6-2-6.9h4c-.2 3.3-1.1 5.7-2 6.9zm2.6-1.3a15 15 0 0 0 1.3-5.6h3a8 8 0 0 1-4.3 5.6z"/></svg>
        www.initiativekorvath-demo.org
      </li>
    </ul>
  </div>
</body>
</html>
```